Marlow Creek sign

24"x36" sign for new home construction job site. Located in affluent in-town neighborhood in Midwest. Traditional american style homes. 2nd generation construction company. Sign needs to convey strength and elegance but not overly elaborate. Competition most has signs consisting of text.

Sign text reads:
Marlow Creek Builders
Custom Luxury for Over 20 years
248-555-0137

Target Market(s)

Upper middle income home buyers

Industry/Entity Type

Construction

Font styles to use
Serif
Decorative

Requirements
Must have
• Logo image no more than 2 colors
Nice to have
• Should be visible and legible from distance of 30'
Should not have
• Not just image of house as logo

```html
<!DOCTYPE html>
<html lang="en">
<head>
<meta charset="utf-8">
<title>Marlow Creek Builders — Job Site Sign</title>
<link href="https://fonts.googleapis.com/css2?family=Alfa+Slab+One&family=Archivo+Black&display=swap" rel="stylesheet">
<style>
  :root {
    --royal-blue: #0b50a0;
    --sky-blue: #40c8f4;
    --gold: #ffc20e;
    --ink: #0a0a0a;
    --silver-light: #e4e4e4;
    --silver-mid: #a9a9a9;
    --silver-dark: #4a4a4a;
  }
  html, body {
    margin: 0;
    padding: 0;
    overflow: hidden;
    background: #ffffff;
  }
  .sign {
    position: relative;
    width: 1200px;
    height: 802px;
    overflow: hidden;
    background: var(--royal-blue);
  }
  .sign__shapes {
    position: absolute;
    inset: 0;
  }
  .sign__corner-ornament {
    position: absolute;
    left: 18px;
    top: 18px;
    width: 140px;
    height: 140px;
    background: linear-gradient(135deg, var(--silver-light), var(--silver-mid));
    clip-path: polygon(0 0, 100% 0, 100% 14%, 14% 14%, 14% 100%, 0 100%);
  }
  .sign__title {
    position: absolute;
    margin: 0;
    font-family: "Alfa Slab One", Georgia, serif;
    font-weight: 400;
    color: var(--gold);
    line-height: 1;
    white-space: nowrap;
  }
  .sign__title--first {
    left: 156px;
    top: 100px;
    font-size: 118px;
    letter-spacing: -1px;
  }
  .sign__title--second {
    left: 404px;
    top: 296px;
    font-size: 122px;
  }
  .sign__mark {
    position: absolute;
    left: 160px;
    top: 270px;
    width: 150px;
    height: 140px;
    border-radius: 8px;
    background: var(--sky-blue);
  }
  .sign__tagline {
    position: absolute;
    left: 0;
    width: 1200px;
    top: 582px;
    margin: 0;
    text-align: center;
    font-family: "Archivo Black", Arial, sans-serif;
    font-size: 35px;
    color: var(--ink);
    white-space: nowrap;
  }
  .sign__phone {
    position: absolute;
    left: 0;
    width: 1200px;
    top: 640px;
    margin: 0;
    text-align: center;
    font-family: "Archivo Black", Arial, sans-serif;
    font-size: 96px;
    line-height: 1;
    letter-spacing: 2px;
    color: var(--ink);
    white-space: nowrap;
  }
</style>
</head>
<body>
<main class="sign">
  <svg class="sign__shapes" width="1200" height="802" viewBox="0 0 1200 802" aria-hidden="true">
    <defs>
      <linearGradient id="silver-rule" x1="0" y1="0" x2="1" y2="0">
        <stop offset="0" stop-color="var(--silver-mid)"/>
        <stop offset="0.5" stop-color="var(--silver-light)"/>
        <stop offset="1" stop-color="var(--silver-mid)"/>
      </linearGradient>
      <linearGradient id="silver-rim" x1="0" y1="0" x2="1" y2="0">
        <stop offset="0" stop-color="var(--silver-dark)"/>
        <stop offset="0.45" stop-color="var(--silver-light)"/>
        <stop offset="0.8" stop-color="var(--silver-mid)"/>
        <stop offset="1" stop-color="var(--silver-dark)"/>
      </linearGradient>
    </defs>
    <!-- frame rules -->
    <rect class="frame-top" x="150" y="32" width="1018" height="9" fill="url(#silver-rule)"/>
    <rect class="frame-top-shadow" x="150" y="41" width="1018" height="3" fill="#1c2a44"/>
    <rect class="frame-right" x="1159" y="32" width="9" height="480" fill="url(#silver-rule)"/>
    <rect class="frame-left" x="32" y="150" width="9" height="640" fill="url(#silver-rule)"/>
    <rect class="frame-left-shadow" x="41" y="150" width="3" height="640" fill="#1c2a44"/>
    <!-- lower panel -->
    <ellipse class="panel-rim" cx="665" cy="922" rx="770" ry="450" fill="url(#silver-rim)"/>
    <ellipse class="panel" cx="645" cy="940" rx="760" ry="450" fill="var(--sky-blue)"/>
  </svg>

  <div class="sign__corner-ornament" role="img" aria-label="Silver scrollwork corner ornament"></div>

  <h1 class="sign__title sign__title--first">Marlow Creek</h1>
  <div class="sign__mark" aria-hidden="true"></div>
  <p class="sign__title sign__title--second">Builders</p>

  <p class="sign__tagline">Custom Luxury for Over 20 years</p>
  <p class="sign__phone">248-555-0137</p>
</main>
</body>
</html>
```